Water Filtration Company needs a business card design using our existing logo/colours!

We design and manufacture and export specialised water filtration equipment. Our equipment will take unclean dirty water and filters to safe clean drinkable water.
We would like to see designs using our existing logo and colours (see attached "Palette") that represents clean safe drinking water (fresh, clean designs but still professional and modern). Our customers are other businesses who supply water filtration equipment, governments, and private individuals.
BUSINESS CARD DETAILS (Common details):
Tel: + 61 7 55 419 276
www: brindlepeak.com.au
Address: 3/47 Cordwell Parade
Marlow Flats NSW 2593 Australia
(please include the word Australia as we are an international company)
Must include: COMMERCIAL WATER FILTRATION EQUIPMENT
NAME NO 1:
Owen Pritch
General Manager
Mobile: +61 427 38 91 04
Email: owen@brindlepeak.com.au
NAME NO. 2:
Gina Rosk
Business Manager
Mobile: +61 409 572 148
Email: gina@brindlepeak.com.au
Must Have:
1) PRINT READY IN .AI & .PDF FORMATS
2) Also saved in file format .ai (Adobe Illustrator - compatible with CS4)
3) Use existing LOGO & COLOURS: Please use our logo (see attached file)
4) FONTS: we have used Avenir & Helvetica in the past but are open to other font types for the address etc.
Thank you!

```html
<!DOCTYPE html>
<html lang="en">
<head>
<meta charset="utf-8">
<title>Brindle Peak – Business Cards</title>
<link rel="stylesheet" href="https://fonts.googleapis.com/css2?family=Nunito+Sans:wght@400;700&display=swap">
<style>
  :root {
    --stage: #0b5d78;
    --card: #ffffff;
    --brand-deep: #0f5c86;
    --brand-teal: #1899bd;
    --band-light: #c9e7ef;
    --band-mid: #4bb5c8;
    --card-w: 540px;
    --card-h: 330px;
  }
  * { margin: 0; padding: 0; box-sizing: border-box; }
  html, body { width: 1200px; height: 960px; overflow: hidden; }
  body {
    background: var(--stage);
    font-family: "Nunito Sans", sans-serif;
    position: relative;
  }
  .card {
    position: absolute;
    left: 330px;
    width: var(--card-w);
    height: var(--card-h);
    background: var(--card);
    overflow: hidden;
    box-shadow: 0 12px 30px rgba(0,0,0,.35);
  }
  .card--front { top: 75px; }
  .card--back { top: 555px; }
  .card__bands { position: absolute; inset: 0; width: 100%; height: 100%; }
  .brand {
    position: absolute;
    display: flex;
    align-items: center;
    gap: 8px;
    color: var(--brand-deep);
    font-weight: 700;
    font-size: 30px;
    letter-spacing: -0.5px;
    line-height: 1;
  }
  .brand__dot {
    width: 14px; height: 14px;
    border-radius: 50%;
    background: var(--brand-teal);
  }
  .card--front .brand { top: 42px; right: 36px; }
  .card--back .brand { top: 130px; left: 40px; font-size: 26px; }
  .contact {
    position: absolute;
    left: 90px;
    top: 196px;
    color: var(--brand-teal);
    font-size: 12.5px;
    line-height: 1.5;
    text-align: center;
  }
  .contact__tagline { font-weight: 700; margin-top: 2px; }
  .person {
    position: absolute;
    left: 262px;
    color: var(--brand-teal);
    font-size: 14px;
    font-weight: 700;
    line-height: 1.3;
  }
  .person--first { top: 60px; }
  .person--second { top: 172px; }
</style>
</head>
<body>

<section class="card card--front">
  <svg class="card__bands" viewBox="0 0 540 330" preserveAspectRatio="none" aria-hidden="true">
    <path fill="var(--band-light)" d="M250 330 C300 250 330 175 400 160 C450 150 500 150 540 110 L540 330 Z"/>
    <path fill="var(--band-mid)" d="M330 330 C420 280 480 220 540 160 L540 330 Z"/>
  </svg>
  <div class="brand"><span class="brand__dot"></span>Brindle Peak</div>
  <div class="contact">
    <p>Tel: + 61 7 55 419 276</p>
    <p>www: brindlepeak.com.au</p>
    <p>Address: 3/47 Cordwell Parade</p>
    <p>Marlow Flats NSW 2593 Australia</p>
    <p class="contact__tagline">COMMERCIAL WATER FILTRATION EQUIPMENT</p>
  </div>
</section>

<section class="card card--back">
  <svg class="card__bands" viewBox="0 0 540 330" preserveAspectRatio="none" aria-hidden="true">
    <path fill="var(--band-light)" d="M0 225 C60 230 110 215 150 250 C180 280 210 310 260 330 L0 330 Z"/>
    <path fill="var(--band-mid)" d="M0 265 C60 290 120 310 190 330 L0 330 Z"/>
  </svg>
  <div class="brand"><span class="brand__dot"></span>Brindle Peak</div>
  <div class="person person--first">
    <p>Owen Pritch</p>
    <p>General Manager</p>
    <p>Mobile: +61 427 38 91 04</p>
    <p>Email: owen@brindlepeak.com.au</p>
  </div>
  <div class="person person--second">
    <p>Gina Rosk</p>
    <p>Business Manager</p>
    <p>Mobile: +61 409 572 148</p>
    <p>Email: gina@brindlepeak.com.au</p>
  </div>
</section>

</body>
</html>
```